Mental Health Non-profit Website that takes donations

We are a faith friendly non profit mental health agency. We need an about us section, a section for taking donations, and a place to list all our therapists and a photo of them
Unfortunately, many of our neighbors in Ohio face mental health challenges which harm their quality of life. Thousands of Ohioans experience trauma, addiction, anxiety, and depression, and the negative outcomes of these experiences continue to grow. While we know that data-driven counseling can improve quality of life for those with mental health challenges, many face economic and social barriers to accessing this transformational care.
Lanterns of Calm crosses barriers to mental health care for Ohioans. We are a nonprofit team of counselors dedicated to employing best practices in modes accessible to people of all backgrounds. A trauma-informed, faith-sensitive methodology uniquely equips us to address holistic mental health challenges. Donor support and community partnerships allow us to meet and serve individuals who could not otherwise access professional care.

Please see our case for support below for more information.

Target Market(s)

Those seeking mental health therapy

Industry/Entity Type

Mental Health Non-profit

Coding

Coded - Design and coding required

Colors

Designer to choose colors to be used in the design.

Requirements
Must have
• Our logo colors of navy blue and gold, our logo, about us section, our mission section, a place to accept donations page for all of our therapists and their pictures, and a place for blog posts

```html
<!DOCTYPE html>
<html lang="en">
<head>
<meta charset="utf-8">
<title>Contact Us – Lanterns of Calm</title>
<link href="https://fonts.googleapis.com/css2?family=Fraunces:opsz,wght@9..144,800;9..144,900&family=Mulish:wght@400;600;700;800&display=swap" rel="stylesheet">
<style>
:root{
  --navy:#0d1b3b;
  --navy-bar:#1e3a68;
  --gold:#e0a106;
  --gold-soft:#e8b73b;
  --ink:#111;
  --text:#2d2d2d;
  --line:#d6d6d6;
  --icon-bg:#e8eef7;
  --white:#fff;
}
*{margin:0;padding:0;box-sizing:border-box}
html,body{width:736px;height:1200px;overflow:hidden;background:var(--white)}
body{position:relative;font-family:"Mulish",sans-serif;color:var(--text)}
.abs{position:absolute}
.serif{font-family:"Fraunces",serif;font-weight:900;color:var(--ink)}

/* hero */
.hero{left:0;top:0;width:736px;height:300px;background:linear-gradient(180deg,#3b3430 0%,#2c2f3a 55%,#23283a 100%)}
.hero-photo{left:0;top:0;width:736px;height:300px;background:radial-gradient(ellipse at 50% 45%,rgba(120,100,85,.55),rgba(20,22,35,.6) 75%)}
.topbar{left:279px;top:0;width:457px;height:20px;background:var(--navy-bar);border-bottom-left-radius:10px;color:var(--white);font-size:8.2px;display:flex;align-items:center}
.topbar .social{display:flex;gap:12px;margin-left:16px}
.topbar .social span{width:8px;height:8px;border:1.2px solid var(--white);border-radius:2px;display:block}
.topbar .contact{margin-left:auto;margin-right:40px;display:flex;gap:14px;align-items:center}
.topbar .contact span{display:flex;align-items:center;gap:4px}
.brand{left:41px;top:14px;width:80px;text-align:center;color:var(--gold-soft);font-size:7.5px;font-weight:700;letter-spacing:.3px;line-height:1.2}
.brand i{display:block;width:30px;height:30px;margin:0 auto 5px;border-radius:50%;background:var(--gold-soft)}
.nav{left:280px;top:33px;display:flex;gap:31px;color:var(--white);font-size:8.3px;font-weight:600;line-height:14px}
.nav .active{color:var(--gold)}
.donate{left:611px;top:27px;width:84px;height:27px;border-radius:14px;background:var(--gold);color:var(--white);font-size:7.8px;font-weight:800;display:flex;align-items:center;justify-content:center}
.hero-title{left:0;width:736px;top:150px;text-align:center;color:var(--white);font-size:29px}
.crumb{left:0;width:736px;top:192px;text-align:center;color:var(--white);font-size:7px}
.crumb em{font-style:normal;color:var(--gold)}

/* contact */
.info-title{left:41px;top:354px;font-size:23.5px;line-height:29px}
.ico{width:25px;height:25px;background:var(--icon-bg);border-radius:3px;display:flex;align-items:center;justify-content:center}
.label{font-size:10.5px}
.val{font-size:10.5px;line-height:14.5px}
.divider{left:327px;top:360px;width:1px;height:247px;background:var(--line)}
.form-title{left:365px;top:354px;font-size:23.5px}
.field{border:1px solid #999;border-radius:15px;font-size:7.4px;color:#444;padding:9px 12px 0}
.submit{left:366px;top:475px;width:162px;height:29px;border-radius:15px;background:var(--gold);color:var(--white);font-size:8.3px;font-weight:800;display:flex;align-items:center;justify-content:center}

/* map */
.map{left:0;top:632px;width:736px;height:307px;background:linear-gradient(135deg,#d8ecd6 0%,#eef2ea 40%,#bfe3ee 60%,#e6efe4 100%)}

/* footer */
.footer{left:0;top:939px;width:736px;height:261px;background:var(--navy)}
.f-brand{left:41px;top:972px;width:156px;text-align:center;color:var(--gold-soft);font-size:14px;font-weight:800;line-height:1.2}
.f-brand i{display:block;width:86px;height:86px;margin:0 auto 10px;border-radius:50%;background:var(--gold-soft)}
.f-brand small{display:block;font-size:8.6px;letter-spacing:3px;font-weight:700}
.f-head{top:966px;font-family:"Fraunces",serif;font-weight:900;color:var(--gold-soft);font-size:12px}
.f-links{left:294px;top:998px;color:var(--white);font-size:9.3px;line-height:21.8px}
.f-item{display:flex;gap:5px;color:var(--white);font-size:9.3px;line-height:14.5px}
.f-ico{width:20px;height:20px;background:var(--gold-soft);border-radius:2px;flex:none;display:flex;align-items:center;justify-content:center}
.f-follow{display:flex;align-items:center;gap:6px;color:var(--white);font-size:8.2px}
.f-follow span.box{width:20px;height:20px;background:#1b2a4c;border-radius:2px;display:flex;align-items:center;justify-content:center}
.f-follow span.box i{width:7px;height:7px;border-radius:50%;background:var(--white)}
.f-rule{left:41px;top:1143px;width:654px;height:1px;background:#2b3a5a}
.copy{left:0;width:736px;top:1157px;text-align:center;color:#cfd4de;font-size:7.8px}
.copy em{font-style:normal;color:var(--gold)}
</style>
</head>
<body>

<header>
  <div class="abs hero"></div>
  <div class="abs hero-photo" role="img" aria-label="Photo of a support group sitting in a circle of chairs in a brick-walled room"></div>
  <div class="abs topbar">
    <div class="social"><span></span><span></span><span></span></div>
    <div class="contact">
      <span><svg width="8" height="8" viewBox="0 0 24 24"><path fill="#e8b73b" d="M6.6 10.8a15 15 0 0 0 6.6 6.6l2.2-2.2c.3-.3.7-.4 1-.2 1.1.4 2.3.6 3.6.6.6 0 1 .4 1 1V20c0 .6-.4 1-1 1A17 17 0 0 1 3 4c0-.6.4-1 1-1h3.5c.6 0 1 .4 1 1 0 1.3.2 2.5.6 3.6.1.3 0 .7-.2 1z"/></svg>(555) 214-0387</span>
      <span><svg width="9" height="8" viewBox="0 0 24 20"><rect x="1" y="1" width="22" height="18" rx="2" fill="none" stroke="#e8b73b" stroke-width="2.4"/><path d="M1 3l11 8 11-8" fill="none" stroke="#e8b73b" stroke-width="2.4"/></svg>hello@lanternsofcalm.org</span>
    </div>
  </div>
  <div class="abs brand"><i></i>LANTERNS OF CALM</div>
  <nav class="abs nav"><span>HOME</span><span>ABOUT US</span><span>THERAPISTS</span><span>BLOG</span><span class="active">CONTACT US</span></nav>
  <div class="abs donate">DONATE NOW</div>
  <h1 class="abs serif hero-title" style="color:#fff">Contact Us</h1>
  <div class="abs crumb">Home &gt; <em>Contact us</em></div>
</header>

<main>
  <section class="contact-info">
    <h2 class="abs serif info-title">Contact<br>Information</h2>
    <div class="abs ico" style="left:41px;top:427px"><svg width="8" height="10" viewBox="0 0 12 16"><path d="M6 0a6 6 0 0 0-6 6c0 4.5 6 10 6 10s6-5.5 6-10a6 6 0 0 0-6-6zm0 8.3A2.3 2.3 0 1 1 6 3.7a2.3 2.3 0 0 1 0 4.6z" fill="#111"/></svg></div>
    <div class="abs serif label" style="left:41px;top:458px">Location</div>
    <div class="abs val" style="left:41px;top:480px">25 Lorem ipsum dolar sit amet Glassglow<br>25KM USA</div>

    <div class="abs ico" style="left:41px;top:527px"><svg width="9" height="9" viewBox="0 0 24 24"><path fill="#111" d="M6.6 10.8a15 15 0 0 0 6.6 6.6l2.2-2.2c.3-.3.7-.4 1-.2 1.1.4 2.3.6 3.6.6.6 0 1 .4 1 1V20c0 .6-.4 1-1 1A17 17 0 0 1 3 4c0-.6.4-1 1-1h3.5c.6 0 1 .4 1 1 0 1.3.2 2.5.6 3.6.1.3 0 .7-.2 1z"/></svg></div>
    <div class="abs serif label" style="left:41px;top:558px">Phone</div>
    <div class="abs val" style="left:41px;top:580px">(555) 214 0387</div>

    <div class="abs ico" style="left:152px;top:527px"><svg width="10" height="8" viewBox="0 0 24 20"><rect x="1" y="1" width="22" height="18" rx="2" fill="none" stroke="#111" stroke-width="2.4"/><path d="M1 3l11 8 11-8" fill="none" stroke="#111" stroke-width="2.4"/></svg></div>
    <div class="abs serif label" style="left:152px;top:558px">Email</div>
    <div class="abs val" style="left:152px;top:580px">hello@lanternsofcalm.org</div>

    <div class="abs divider"></div>
  </section>

  <section class="contact-form">
    <h2 class="abs serif form-title">Get In Touch with Us</h2>
    <div class="abs field" style="left:366px;top:401px;width:162px;height:29px">Name:</div>
    <div class="abs field" style="left:533px;top:401px;width:162px;height:29px">Phone:</div>
    <div class="abs field" style="left:366px;top:438px;width:162px;height:29px">Email:</div>
    <div class="abs field" style="left:533px;top:438px;width:162px;height:66px;border-radius:15px">Message:</div>
    <div class="abs submit">SUBMIT</div>
  </section>

  <div class="abs map" role="img" aria-label="Street map showing the office location"></div>
</main>

<footer>
  <div class="abs footer"></div>
  <div class="abs f-brand"><i></i>LANTERNS OF CALM<small>BEHAVIORAL HEALTH</small></div>

  <div class="abs f-head" style="left:294px">Quick Links</div>
  <div class="abs f-links">Home<br>About Us<br>Therapist<br>Blog<br>Contact Us</div>

  <div class="abs f-head" style="left:426px">Contact Us</div>
  <div class="abs f-item" style="left:426px;top:998px;width:180px"><span class="f-ico"><svg width="7" height="9" viewBox="0 0 12 16"><path d="M6 0a6 6 0 0 0-6 6c0 4.5 6 10 6 10s6-5.5 6-10a6 6 0 0 0-6-6zm0 8.3A2.3 2.3 0 1 1 6 3.7a2.3 2.3 0 0 1 0 4.6z" fill="#fff"/></svg></span>25 Lorem ipsum dolar sit amet Glassglo 25KM SUA</div>
  <div class="abs f-item" style="left:426px;top:1048px;align-items:center"><span class="f-ico"><svg width="8" height="8" viewBox="0 0 24 24"><path fill="#fff" d="M6.6 10.8a15 15 0 0 0 6.6 6.6l2.2-2.2c.3-.3.7-.4 1-.2 1.1.4 2.3.6 3.6.6.6 0 1 .4 1 1V20c0 .6-.4 1-1 1A17 17 0 0 1 3 4c0-.6.4-1 1-1h3.5c.6 0 1 .4 1 1 0 1.3.2 2.5.6 3.6.1.3 0 .7-.2 1z"/></svg></span>(555) 214-0387</div>
  <div class="abs f-item" style="left:426px;top:1084px;align-items:center"><span class="f-ico"><svg width="9" height="7" viewBox="0 0 24 20"><rect x="1" y="1" width="22" height="18" rx="2" fill="none" stroke="#fff" stroke-width="2.4"/><path d="M1 3l11 8 11-8" fill="none" stroke="#fff" stroke-width="2.4"/></svg></span>hello@lanternsofcalm.org</div>

  <div class="abs f-head" style="left:632px">Follow Us</div>
  <div class="abs f-follow" style="left:632px;top:1001px"><span class="box"><i></i></span>Socialpage</div>
  <div class="abs f-follow" style="left:632px;top:1029px"><span class="box"><i></i></span>Photogram</div>
  <div class="abs f-follow" style="left:632px;top:1057px"><span class="box"><i></i></span>Worklink</div>

  <div class="abs f-rule"></div>
  <div class="abs copy">© <em>LANTERNS OF CALM</em>, 2024. ALL RIGHTS RESERVED.</div>
</footer>

</body>
</html>
```